Need full color yard sign designed

I need a catchy yard sign to attract people whom drive by to go to the website www.brickleafestimates.net to get a free no obligation value of their home. I like to use the location icon as part of the design. The design must be in both spanish and english top and bottom split design. I have attached the template format that the printing company needs me to use. I also need it in eps format. Also the sign will be double sided so same sign will be on both sidesPlease let me know if you have any questions about the design

Target Market(s)

Home owners looking to sell

Industry/Entity Type

Real Estate

Font styles to use
Sans Serif

Colors
f68d4d
fbed22
9bcb3b
0692cd

Requirements
Must have
• call to action theme. light colors since this is a sign and must also be seen at night
Nice to have
• colorful
Should not have
• dark background, too busy

```html
<!DOCTYPE html>
<html lang="en">
<head>
<meta charset="utf-8">
<title>Yard Sign – Free Home Value</title>
<link rel="stylesheet" href="https://fonts.googleapis.com/css2?family=Source+Sans+3:wght@400;500;700&display=swap">
<style>
  :root {
    --sign-orange: #e07a24;
    --band-red: #a51e24;
    --pin-black: #262626;
    --text-white: #ffffff;
    --divider: #9c2a1c;
  }
  html, body {
    margin: 0;
    padding: 0;
    width: 1200px;
    height: 900px;
    overflow: hidden;
    background: var(--sign-orange);
  }
  .sign {
    position: relative;
    width: 1200px;
    height: 900px;
    background: var(--sign-orange);
    font-family: "Source Sans 3", "Myriad Pro", sans-serif;
    color: var(--text-white);
    overflow: hidden;
  }
  .panel {
    position: absolute;
    left: 0;
    width: 1200px;
    height: 450px;
  }
  .panel--english { top: 0; }
  .panel--spanish { top: 466px; height: 434px; }

  .headline {
    position: absolute;
    left: 61px;
    top: 50px;
    margin: 0;
    font-weight: 500;
    font-size: 44px;
    line-height: 57px;
    letter-spacing: 0.3px;
  }
  .panel--spanish .headline { top: 36px; }

  .url-band {
    position: absolute;
    left: 0;
    width: 1200px;
    height: 68px;
    background: var(--band-red);
  }
  .panel--english .url-band { top: 216px; }
  .panel--spanish .url-band { top: 216px; }

  .url {
    position: absolute;
    left: 62px;
    top: 0;
    margin: 0;
    font-weight: 700;
    font-size: 62px;
    line-height: 68px;
    letter-spacing: -0.6px;
    white-space: nowrap;
  }

  .offer {
    position: absolute;
    left: 62px;
    top: 318px;
    margin: 0;
    font-weight: 500;
    font-size: 38px;
    line-height: 46px;
    white-space: nowrap;
  }
  .panel--spanish .offer { top: 318px; }

  .pin {
    position: absolute;
    left: 970px;
    top: 112px;
    width: 200px;
    height: 262px;
  }

  .divider {
    position: absolute;
    left: 40px;
    top: 451px;
    width: 1120px;
    height: 2px;
    background: linear-gradient(to right, rgba(156,42,28,0), var(--divider) 20%, var(--divider) 80%, rgba(156,42,28,0));
  }
</style>
</head>
<body>
<main class="sign">

  <section class="panel panel--english" lang="en">
    <h1 class="headline">How much is your home worth<br>in today’s market?</h1>
    <div class="url-band">
      <p class="url">www.brickleafestimates.net</p>
    </div>
    <p class="offer">To get a free No Obligation Value of their home</p>
    <svg class="pin" viewBox="0 0 200 262" aria-hidden="true">
      <path d="M92 254 C 110 200, 150 170, 188 150 C 196 130, 180 110, 160 104 L 140 130 Z" fill="#000" opacity="0.2"/>
      <path d="M84 254 C 76 206, 46 166, 20 126 A78 78 0 1 1 148 126 C 122 166, 92 206, 84 254 Z" fill="var(--pin-black)"/>
      <circle cx="84" cy="80" r="27" fill="#fff"/>
    </svg>
  </section>

  <div class="divider"></div>

  <section class="panel panel--spanish" lang="es">
    <h2 class="headline">Spanish text to come here<br>Spanish text to come?</h2>
    <div class="url-band">
      <p class="url">www.brickleafestimates.net</p>
    </div>
    <p class="offer">To get a free No Obligation Value of their home</p>
    <svg class="pin" viewBox="0 0 200 262" aria-hidden="true">
      <path d="M92 254 C 110 200, 150 170, 188 150 C 196 130, 180 110, 160 104 L 140 130 Z" fill="#000" opacity="0.2"/>
      <path d="M84 254 C 76 206, 46 166, 20 126 A78 78 0 1 1 148 126 C 122 166, 92 206, 84 254 Z" fill="var(--pin-black)"/>
      <circle cx="84" cy="80" r="27" fill="#fff"/>
    </svg>
  </section>

</main>
</body>
</html>
```